Kanomiva business cards/stationary
Relocation Support Services
I need single sided standard sized Business Card [3.5" x 2"]
Designer's discretion
Professional
Ned Palmer
President
5-31-08 Nishimorino
Suginami-ku, Tokyo 168-0072
ned@kanomiva.com
www.kanomiva.com
Have not yet received logo files from designer. I will be using
Will upload Al format as soon as I receive from designer.
Kanomiva logo to be used

```html
<!DOCTYPE html>
<html lang="en">
<head>
<meta charset="utf-8">
<title>Kanomiva – Business Card</title>
<link href="https://fonts.googleapis.com/css2?family=Source+Sans+3:wght@400;600;700&display=swap" rel="stylesheet">
<style>
  :root {
    --bg: #e9e7e3;
    --card: #ffffff;
    --brand-red: #d01f2e;
    --deep-red: #a8141f;
    --text-grey: #6d6d6d;
    --white: #ffffff;
  }
  html, body {
    margin: 0;
    width: 1200px;
    height: 778px;
    overflow: hidden;
    background: var(--bg);
    font-family: "Source Sans 3", Arial, sans-serif;
  }
  .business-card {
    position: absolute;
    left: 100px;
    top: 103px;
    width: 1000px;
    height: 572px;
    background: var(--card);
    border-radius: 32px;
    overflow: hidden;
    box-shadow: 0 6px 18px rgba(0,0,0,0.18);
  }
  .lower-band {
    position: absolute;
    left: 0;
    right: 0;
    top: 300px;
    bottom: 0;
    background: linear-gradient(90deg, var(--brand-red), var(--deep-red));
  }
  .brand {
    position: absolute;
    left: 78px;
    top: 140px;
    display: flex;
    align-items: center;
    gap: 22px;
  }
  .brand-dot {
    width: 76px;
    height: 76px;
    border-radius: 50%;
    background: var(--brand-red);
  }
  .brand-name {
    font-size: 60px;
    font-weight: 700;
    color: var(--brand-red);
    letter-spacing: -1px;
  }
  .holder {
    position: absolute;
    right: 60px;
    top: 66px;
    text-align: right;
  }
  .holder-name {
    font-size: 36px;
    font-weight: 700;
    color: var(--brand-red);
    line-height: 1.1;
  }
  .holder-title {
    font-size: 28px;
    font-weight: 600;
    color: var(--text-grey);
    line-height: 1.3;
  }
  .contact {
    position: absolute;
    right: 30px;
    top: 330px;
    color: var(--white);
    font-size: 26px;
    line-height: 36px;
    text-align: right;
  }
  .address { margin-bottom: 24px; padding-right: 48px; }
  .contact-line {
    display: flex;
    justify-content: flex-end;
    align-items: center;
    gap: 22px;
  }
  .contact-icon {
    width: 26px;
    height: 26px;
    flex: none;
  }
</style>
</head>
<body>
  <div class="business-card">
    <div class="lower-band" role="img" aria-label="Red and grey swoosh band across the lower card"></div>

    <div class="brand">
      <span class="brand-dot"></span>
      <span class="brand-name">Kanomiva</span>
    </div>

    <div class="holder">
      <div class="holder-name">Ned Palmer</div>
      <div class="holder-title">President</div>
    </div>

    <div class="contact">
      <div class="address">5-31-08 Nishimorino<br>Suginami-ku, Tokyo 168-0072</div>
      <div class="contact-line">
        <span>+81 (0)80-4392-5816</span>
        <svg class="contact-icon" viewBox="0 0 24 24" aria-hidden="true"><path fill="#fff" d="M6.6 10.8a15.1 15.1 0 0 0 6.6 6.6l2.2-2.2a1 1 0 0 1 1-.25 11.4 11.4 0 0 0 3.6.57 1 1 0 0 1 1 1V20a1 1 0 0 1-1 1A17 17 0 0 1 3 4a1 1 0 0 1 1-1h3.5a1 1 0 0 1 1 1c0 1.25.2 2.45.57 3.6a1 1 0 0 1-.25 1z"/></svg>
      </div>
      <div class="contact-line">
        <span>ned@kanomiva.com</span>
        <svg class="contact-icon" viewBox="0 0 24 24" aria-hidden="true"><rect x="2" y="5" width="20" height="14" rx="1.5" fill="#fff"/><path d="M3 6l9 7 9-7" fill="none" stroke="#b8171f" stroke-width="1.8"/></svg>
      </div>
      <div class="contact-line">
        <span>www.kanomiva.com</span>
        <svg class="contact-icon" viewBox="0 0 24 24" aria-hidden="true"><circle cx="12" cy="12" r="10" fill="#fff"/><path d="M2 12h20M12 2c3 3 3 17 0 20M12 2c-3 3-3 17 0 20" fill="none" stroke="#b8171f" stroke-width="1.5"/></svg>
      </div>
    </div>
  </div>
</body>
</html>
```